Stationary Set and Logo Update **PAYMENT GUARANTEED**

Stationery Design and Logo Update

About Us

Trindex Supply is a wholesale distributor of OEM [original brand] and compatible [generic brand] parts and supplies for use in copiers, faxes, printers, and multi-function machines. In plain English…we sell all the parts and supplies [such as toner] that make up any office equipment which outputs an image on paper.

Trindex was the 1st distributor to develop and sell a generic brand copier part in the United States. We have been in business since 1972 [nearly 40 years]. Our tagline is "The Steady Choice," as in our company was the first alternative product that copier dealers had to buying original brand copier parts. Trindex is known for offering reliable and cost-effective OEM and compatible products.

Project

We require a fresh, modern and corporate identity. Please submit a stationary package inclusive of a double-sided business card (2" x 3.5"), letterhead (8.5'x11"), and standard #10 envelope (4-1/8” x 9-1/2). You may use our current logo or preferably your take on an updated one. If an attempt is made in updating the logo #004D8E or a similar hue should be used as the primary color.

The design should be clean, simple, modern and professional and make an immediate impact.

Target Market(s)

Copier and printer dealers who lease and service imaging equipment in the United States and Latin America.

Industry/Entity Type

Business

Requirements
Must have
• Simple, clean, modern and professional. Please use #004D8E or a similar hue as the primary color. Letterhead must accommate (2) addresses. We have 2 locations.
Nice to have
• A simple, modern update to our current logo. https://assets.mailvorbo.example/fs030/5520384417702/img/418.jpg
Should not have
• More than (2) colors on logo.

```html
<!DOCTYPE html>
<html lang="en">
<head>
<meta charset="utf-8">
<title>Trindex Stationery Set</title>
<link href="https://fonts.googleapis.com/css2?family=Montserrat:wght@400;600;700&display=swap" rel="stylesheet">
<style>
  :root{
    --brand:#004D8E;
    --accent:#0a9ad6;
    --text-grey:#9a9a9a;
    --stage:#f4f4f4;
    --paper:#ffffff;
    --edge:#2a2a2a;
  }
  html,body{margin:0;padding:0;overflow:hidden;background:#fff;}
  .canvas{position:relative;width:1200px;height:995px;overflow:hidden;font-family:"Montserrat",sans-serif;}
  .stage{position:absolute;left:34px;top:0;width:1166px;height:816px;background:var(--stage);}
  .sheet{position:absolute;background:var(--paper);border:2px solid var(--edge);box-sizing:border-box;}
  .wordmark{position:absolute;color:var(--brand);font-family:"Montserrat",sans-serif;font-weight:700;letter-spacing:-0.5px;line-height:1;white-space:nowrap;}
  .contact{position:absolute;color:var(--text-grey);font-size:8px;line-height:10px;letter-spacing:.2px;}
  .contact h3{margin:0 0 1px;font-size:9.5px;font-weight:600;line-height:12px;}
  .contact p{margin:0 0 6px;}
  .contact b{font-weight:600;}
  .contact .gap{margin-top:12px;}

  .letterhead{left:134px;top:26px;width:594px;height:769px;}
  .letterhead .wordmark{left:374px;top:30px;font-size:35px;}
  .letterhead .contact{left:462px;top:86px;font-size:8.5px;line-height:10.5px;}
  .letterhead .contact h3{font-size:11px;line-height:14px;}
  .letterhead .contact p{margin-bottom:8px;}

  .envelope{left:360px;top:419px;width:664px;height:288px;}
  .envelope .wordmark{left:16px;top:27px;font-size:24px;}
  .envelope .contact{left:16px;top:64px;font-size:7px;line-height:9.2px;}
  .envelope .contact h3{font-size:8px;line-height:11px;}

  .card-front{left:557px;top:321px;width:245px;height:140px;}
  .card-front .wordmark{left:30px;top:50px;font-size:37px;}
  .card-front .person{position:absolute;left:127px;top:93px;font-size:9px;line-height:11px;}
  .card-front .person .name{color:var(--brand);font-weight:600;margin:0;}
  .card-front .person .role{color:var(--accent);font-size:7.5px;margin:0;}

  .card-back{left:810px;top:262px;width:141px;height:245px;}
  .card-back .wordmark{left:11px;top:36px;font-size:24px;}
  .card-back .contact{left:11px;top:71px;font-size:7px;line-height:9.2px;}
  .card-back .contact h3{font-size:8px;line-height:11px;}

  .hero-mark{left:829px;top:58px;font-size:76px;}
</style>
</head>
<body>
<div class="canvas">
  <div class="stage"></div>

  <section class="sheet letterhead" aria-label="Letterhead">
    <div class="wordmark">Trindex</div>
    <div class="contact">
      <h3>Corporate Office</h3>
      <p>2187 Northwest 52nd Avenue<br>Fort Lauderdale, FL 33309</p>
      <p><b>Toll Free:</b> 800.555.0142<br><b>Local:</b> 954.555.0187<br><b>Fax:</b> 954.555.0193</p>
      <h3 class="gap">Trindex West</h3>
      <p>Sierra Ridge Industrial Park #4<br>1640 Larkin Way<br>Reno, NV 89502</p>
      <p><b>Toll Free:</b> 800.555.0166<br><b>Fax:</b> 775.555.0128</p>
    </div>
  </section>

  <section class="sheet envelope" aria-label="Envelope">
    <div class="wordmark">Trindex</div>
    <div class="contact">
      <h3>Corporate Office</h3>
      <p>2187 Northwest 52nd Avenue<br>Fort Lauderdale, FL 33309<br>Toll Free: 800.555.0142<br>Local: 954.555.0187<br>Fax: 954.555.0193</p>
      <h3>Trindex West</h3>
      <p>Sierra Ridge Industrial Park #4<br>1640 Larkin Way<br>Reno, NV 89502<br>Toll Free: 800.555.0166<br>Fax: 775.555.0128</p>
    </div>
  </section>

  <section class="sheet card-front" aria-label="Business card front">
    <div class="wordmark">Trindex</div>
    <div class="person">
      <p class="name">Marisol Fenwick</p>
      <p class="role">Marketing Coordinator</p>
    </div>
  </section>

  <section class="sheet card-back" aria-label="Business card back">
    <div class="wordmark">Trindex</div>
    <div class="contact">
      <h3>Corporate Office</h3>
      <p>2187 Northwest 52nd Avenue<br>Fort Lauderdale, FL 33309<br>Toll Free: 800.555.0142<br>Local: 954.555.0187<br>Fax: 954.555.0193</p>
      <h3>Trindex West</h3>
      <p>Sierra Ridge Industrial Park #4<br>1640 Larkin Way<br>Reno, NV 89502<br>Toll Free: 800.555.0166<br>Fax: 775.555.0128</p>
    </div>
  </section>

  <div class="wordmark hero-mark">Trindex</div>
</div>
</body>
</html>
```